Business Card Design Project

I need a new business card design for my building/development company: Kestrel Ridge Builders.

We specialise in small sub-divisions, multi-story developments and new house builds.
We handle the whole process from concept stage right throught to a fully developed property.
Updates

Target Market(s)

people looking to develop their property and need help. New property buyers

Industry/Entity Type

House

Requirements
Must have
• My logo on both sides:
Side 1: Logo taking up whole side as per old card but with a color/style change.

Side 2: Contact page: include logo but the rest just surprise me!

All contact details will be: (and need to be changable for each employee) I'll inform you of specifics before printing.

Name Surname
Position ie. Managing director
M: insert mobile
E: insert email
P.O. Box 518, Ashwell, Vic, 3094
www.kestrelridgebuilders.com.au

Nice to have
• Colors i'd like: (not necessarily all but this is the basic idea)

Black, blue, grey, silver, white

```html
<!DOCTYPE html>
<html lang="en">
<head>
<meta charset="utf-8">
<title>Kestrel Ridge Builders – Business Card</title>
<link href="https://fonts.googleapis.com/css2?family=Source+Sans+3:wght@400;600;700&display=swap" rel="stylesheet">
<style>
  :root {
    --stage: #7d7d7d;
    --brand-blue: #0a8dd6;
    --ink: #111111;
    --paper: #ffffff;
    --tab-dark: #050505;
  }
  * { margin: 0; padding: 0; box-sizing: border-box; }
  html, body {
    width: 1200px;
    height: 900px;
    overflow: hidden;
    background: var(--stage);
    font-family: "Source Sans 3", "Helvetica Neue", Arial, sans-serif;
  }
  .card {
    position: absolute;
    left: 308px;
    width: 590px;
    height: 335px;
    overflow: hidden;
  }
  .card-front { top: 80px; background: var(--brand-blue); }
  .card-back { top: 496px; background: var(--paper); }

  .tab {
    position: absolute;
    left: 62px;
    width: 468px;
    height: 14px;
  }
  .tab-top { top: 0; border-radius: 0 0 28px 28px; }
  .tab-bottom { bottom: 0; border-radius: 28px 28px 0 0; }
  .card-front .tab { background: var(--tab-dark); }
  .card-back .tab { background: var(--brand-blue); }

  /* Front */
  .front-brand {
    position: absolute;
    top: 170px;
    left: 0;
    width: 100%;
    text-align: center;
  }
  .front-brand .brand-name {
    font-size: 38px;
    font-weight: 600;
    color: var(--paper);
    line-height: 1;
    letter-spacing: -0.5px;
  }
  .front-brand .tagline {
    font-size: 15px;
    color: var(--ink);
    margin-top: 4px;
  }
  .front-web {
    position: absolute;
    top: 262px;
    left: 0;
    width: 100%;
    text-align: center;
    font-size: 16px;
    color: var(--ink);
  }
  .front-web::after {
    content: "";
    display: block;
    width: 280px;
    height: 2px;
    margin: 7px auto 0;
    background: linear-gradient(to right, transparent, rgba(255,255,255,0.9), transparent);
  }

  /* Back */
  .back-brand {
    position: absolute;
    top: 146px;
    left: 30px;
    width: 260px;
    text-align: center;
  }
  .back-brand .brand-name {
    font-size: 25px;
    font-weight: 600;
    color: var(--brand-blue);
    line-height: 1;
    letter-spacing: -0.3px;
  }
  .back-brand .tagline {
    font-size: 11px;
    color: var(--ink);
    margin-top: 3px;
  }
  .person {
    position: absolute;
    top: 86px;
    left: 359px;
    color: var(--ink);
  }
  .person .full-name { font-size: 24px; line-height: 1.1; }
  .person .position { font-size: 16px; font-weight: 700; margin-top: 5px; }
  .contact {
    position: absolute;
    top: 207px;
    left: 335px;
    list-style: none;
    font-size: 14.5px;
    line-height: 20px;
    color: var(--ink);
  }
  .contact b { font-weight: 700; }
</style>
</head>
<body>
  <section class="card card-front">
    <div class="tab tab-top"></div>
    <div class="front-brand">
      <div class="brand-name">Kestrel Ridge Builders</div>
      <div class="tagline">renovation-construction-development</div>
    </div>
    <div class="front-web">www.kestrelridgebuilders.com.au</div>
    <div class="tab tab-bottom"></div>
  </section>

  <section class="card card-back">
    <div class="tab tab-top"></div>
    <div class="back-brand">
      <div class="brand-name">Kestrel Ridge Builders</div>
      <div class="tagline">renovation-construction-development</div>
    </div>
    <div class="person">
      <div class="full-name">Name Surname</div>
      <div class="position">Position</div>
    </div>
    <ul class="contact">
      <li><b>T.P :</b> insert t:p number</li>
      <li><b>M :</b> insert mobile</li>
      <li><b>E :</b> insert email</li>
      <li>P.O. Box 518, Ashwell, Vic, 3094</li>
    </ul>
    <div class="tab tab-bottom"></div>
  </section>
</body>
</html>
```